Business Card Design - Law Firm

We are a boutique law firm located near the beach in Manly, Australia. We have recently had a new logo designed and are revamping our business cards with the new logo.

We have recently had a business card design done for us but are not entirely happy with it. We are looking for something modern, simplistic but striking. We would like to see multiple designs.

We have attached a word document which includes our new logo and the current business card design which we are looking at moving away from.

We would like the business cards to be double sided. We would like the design to include something which we can print in gloss colour when we send it to the business card printers.

```html
<!DOCTYPE html>
<html lang="en">
<head>
<meta charset="utf-8">
<title>Harwell &amp; Partners Lawyers – Business Card</title>
<link rel="stylesheet" href="https://fonts.googleapis.com/css2?family=Raleway:wght@500;600&family=Open+Sans:wght@400;700&display=swap">
<style>
  :root {
    --backdrop: #242424;
    --card-white: #f3f3f3;
    --navy: #2b3584;
    --navy-deep: #2f3f85;
    --wave-blue: #6a7fc2;
    --sand: #b3a667;
    --sand-light: #cdb883;
    --ink: #1c1c1c;
  }
  * { box-sizing: border-box; margin: 0; padding: 0; }
  html, body { width: 1200px; height: 900px; overflow: hidden; }
  body {
    background: var(--backdrop);
    position: relative;
    font-family: "Open Sans", Arial, sans-serif;
    color: var(--ink);
  }
  .card {
    position: absolute;
    top: 200px;
    width: 310px;
    height: 502px;
    overflow: hidden;
  }
  .card--front {
    left: 253px;
    background: var(--card-white);
    border-radius: 62px 0 62px 0;
  }
  .card--back {
    left: 627px;
    border-radius: 0 62px 0 62px;
  }
  .brand {
    position: absolute;
    left: 0;
    width: 100%;
    text-align: center;
    font-family: "Raleway", Arial, sans-serif;
  }
  .brand__mark {
    display: block;
    width: 46px;
    height: 46px;
    margin: 0 auto 22px;
    border-radius: 50%;
    background: var(--navy);
  }
  .brand__name {
    font-weight: 600;
    font-size: 17px;
    letter-spacing: 1px;
    color: var(--ink);
  }
  .brand__tag {
    font-weight: 500;
    font-size: 11px;
    letter-spacing: 7px;
    padding-left: 7px;
    margin-top: 2px;
    color: var(--ink);
  }
  .card--front .brand { top: 112px; padding-left: 10px; }
  .card--back .brand { top: 410px; }

  .contact {
    position: absolute;
    left: 33px;
    top: 296px;
    font-size: 13px;
    line-height: 18px;
  }
  .contact__name {
    font-weight: 700;
    font-size: 18px;
    line-height: 22px;
    color: var(--navy);
  }
  .contact__role { margin-left: 2px; margin-bottom: 6px; }
  .contact__firm {
    font-weight: 700;
    color: var(--navy);
  }
  .contact__address { margin-bottom: 6px; }
  .contact__address .spaced { word-spacing: 12px; }
  .contact__line { display: flex; align-items: center; gap: 6px; }
  .contact__line svg { width: 13px; height: 13px; flex: none; }

  .back-art { position: absolute; inset: 0; }
</style>
</head>
<body>

  <section class="card card--front">
    <div class="brand">
      <span class="brand__mark"></span>
      <div class="brand__name">Harwell &amp; Partners</div>
      <div class="brand__tag">LAWYERS</div>
    </div>

    <div class="contact">
      <div class="contact__name">MAYA ELLISON</div>
      <div class="contact__role">Practice Manager</div>
      <div class="contact__firm">HARWELL &amp; PARTNERS</div>
      <div class="contact__address">
        Suite 4, 12 Tidewater Lane<br>
        <span class="spaced">COVELY NSW 2099</span>
      </div>
      <div class="contact__line">
        <svg viewBox="0 0 16 16" aria-hidden="true"><path fill="#2b3584" d="M2 6c0-2 3-3 6-3s6 1 6 3v1h-3V5.5H5V7H2zM4 8h8l1 5H3z"/><circle cx="8" cy="10.5" r="1.4" fill="#f3f3f3"/></svg>
        <span>(02) 9000 4811</span>
      </div>
      <div class="contact__line">
        <svg viewBox="0 0 16 16" aria-hidden="true"><path fill="#2b3584" d="M4 1h8v4H4zM1 6h14v6h-2v3H3v-3H1zM5 10v3h6v-3z"/></svg>
        <span>(02) 9000 4822</span>
      </div>
      <div class="contact__line">
        <svg viewBox="0 0 16 16" aria-hidden="true"><circle cx="8" cy="8" r="7" fill="#2b3584"/><path fill="#f3f3f3" d="M5 4c2 0 3 1 2 3s-3 1-3 3c-1-2-1-4 1-6zm5 4c2 0 3 1 2 3-1 1-2 2-3 2 0-2 2-2 1-5z"/></svg>
        <span>www.harwellpartners.com.au</span>
      </div>
    </div>
  </section>

  <section class="card card--back">
    <svg class="back-art" viewBox="0 0 310 502" preserveAspectRatio="none" role="img" aria-label="Flowing wave decoration in navy, light blue and sand gold">
      <defs>
        <linearGradient id="back-tone" x1="0" y1="0" x2="0" y2="1">
          <stop offset="0" stop-color="#2f3f85"/>
          <stop offset="0.45" stop-color="#4a5ea6"/>
          <stop offset="0.62" stop-color="#7a8fc9"/>
          <stop offset="0.72" stop-color="#c2b27c"/>
          <stop offset="1" stop-color="#b3a667"/>
        </linearGradient>
      </defs>
      <rect width="310" height="502" fill="url(#back-tone)"/>
    </svg>
    <div class="brand">
      <div class="brand__name">Harwell &amp; Partners</div>
      <div class="brand__tag">LAWYERS</div>
    </div>
  </section>

</body>
</html>
```